Brightbay Business Card Design

Our company is called Brightbay. We manufacture confectionary snacks & frozen novelties. Our initial product portfolio includes frozen ice lollies/popsicles & stick ice cream bars.

We require a business card design.

Please use the attached Logo.

Please use an orange, brown, yellow colour code. You may choose any combination of the 3 or include all three. The logo however must remain orange.

Target Market(s)

Business card will be targeted at distributors of our products such as supermarket procurement managers, convenience store owners, wholesale distributors and merchandising agents.

Industry/Entity Type

Business

Requirements
Must have
• Calvin Obeng_Director/ P.O.Box Dunmore 5172, Accra, Ghana / m: 00233(0)507318924/ e: calvin.obeng@mailvora.co.uk

```html
<!DOCTYPE html>
<html lang="en">
<head>
<meta charset="utf-8">
<title>Brightbay Business Card</title>
<link rel="stylesheet" href="https://fonts.googleapis.com/css2?family=Montserrat:wght@400;500;700&display=swap">
<style>
  :root {
    --stage: #d9d9d9;
    --card-white: #f7f7f7;
    --card-brown: #5c2a15;
    --brand-orange: #e8641c;
    --ink: #2b2b2b;
    --ink-soft: #3a3a3a;
  }
  * { box-sizing: border-box; margin: 0; padding: 0; }
  html, body {
    width: 1200px;
    height: 900px;
    overflow: hidden;
    background: var(--stage);
    font-family: "Montserrat", Arial, sans-serif;
  }
  .stage {
    width: 1200px;
    height: 900px;
    display: flex;
    flex-direction: column;
    align-items: center;
    justify-content: center;
    gap: 50px;
  }
  .card {
    width: 630px;
    height: 360px;
    border-radius: 24px;
    box-shadow: 0 6px 18px rgba(0,0,0,0.18);
    position: relative;
  }
  .card--back {
    background: var(--card-brown);
    display: flex;
    align-items: center;
    justify-content: center;
  }
  .card--front {
    background: var(--card-white);
  }
  .brand {
    display: flex;
    align-items: center;
    gap: 12px;
    color: var(--brand-orange);
    font-weight: 700;
    letter-spacing: -0.5px;
  }
  .brand__dot {
    border-radius: 50%;
    background: var(--brand-orange);
    flex: none;
  }
  .card--back .brand { font-size: 52px; }
  .card--back .brand__dot { width: 44px; height: 44px; }
  .card--front .brand {
    position: absolute;
    left: 40px;
    top: 150px;
    font-size: 40px;
  }
  .card--front .brand__dot { width: 34px; height: 34px; }
  .identity {
    position: absolute;
    left: 330px;
    top: 78px;
    width: 270px;
  }
  .identity__name {
    font-size: 24px;
    font-weight: 400;
    color: var(--ink);
    letter-spacing: 0.5px;
    line-height: 1.1;
  }
  .identity__role {
    font-size: 15px;
    color: var(--ink-soft);
    margin-top: 2px;
  }
  .identity__rule {
    height: 1.5px;
    background: var(--brand-orange);
    margin-top: 14px;
    width: 300px;
  }
  .contact-list {
    list-style: none;
    position: absolute;
    left: 330px;
    top: 200px;
  }
  .contact-list__item {
    display: flex;
    align-items: flex-start;
    gap: 12px;
    font-size: 15px;
    color: var(--ink);
    line-height: 1.15;
    margin-bottom: 12px;
    letter-spacing: 0.3px;
  }
  .contact-list__icon {
    width: 22px;
    height: 22px;
    flex: none;
  }
</style>
</head>
<body>
<main class="stage">
  <section class="card card--back" aria-label="Business card back">
    <div class="brand"><span class="brand__dot"></span><span class="brand__name">Brightbay</span></div>
  </section>

  <section class="card card--front" aria-label="Business card front">
    <div class="brand"><span class="brand__dot"></span><span class="brand__name">Brightbay</span></div>

    <div class="identity">
      <h1 class="identity__name">Calvin Obeng</h1>
      <p class="identity__role">Director</p>
      <div class="identity__rule"></div>
    </div>

    <ul class="contact-list">
      <li class="contact-list__item">
        <svg class="contact-list__icon" viewBox="0 0 22 22" aria-hidden="true">
          <circle cx="11" cy="11" r="11" fill="var(--brand-orange)"/>
          <path d="M8 6.5l1.6 2.4-1 1.2c.7 1.4 1.8 2.5 3.2 3.2l1.2-1 2.4 1.6-.8 1.8c-3.8-.4-7.4-4-7.8-7.8z" fill="#fff"/>
        </svg>
        <span>00233(0)507318924</span>
      </li>
      <li class="contact-list__item">
        <svg class="contact-list__icon" viewBox="0 0 22 22" aria-hidden="true">
          <circle cx="11" cy="11" r="11" fill="var(--brand-orange)"/>
          <rect x="5.5" y="7" width="11" height="8" fill="none" stroke="#fff" stroke-width="1.3"/>
          <path d="M5.5 7l5.5 4.5L16.5 7" fill="none" stroke="#fff" stroke-width="1.3"/>
        </svg>
        <span>calvin.obeng@mailvora.co.uk</span>
      </li>
      <li class="contact-list__item">
        <svg class="contact-list__icon" viewBox="0 0 22 22" aria-hidden="true">
          <circle cx="11" cy="11" r="11" fill="var(--brand-orange)"/>
          <path d="M11 5a4 4 0 0 1 4 4c0 3-4 7.5-4 7.5S7 12 7 9a4 4 0 0 1 4-4z" fill="#fff"/>
          <circle cx="11" cy="9" r="1.5" fill="var(--brand-orange)"/>
        </svg>
        <span>P.O.Box Dunmore 5172,<br>Accra, Ghana</span>
      </li>
    </ul>
  </section>
</main>
</body>
</html>
```